business card double side design

We need a business card design for our company PLUMlearnhub. DOUBLE SIDED. We provide continuing education programs & courses across North America. Our website is www.plumlearnhub.example - please use the grey pinstrip concept as part of the design. Compliment the branding that is occuring on that site!
Please use pantones daa520 and 3f3151. Verdana for text. I have attached our logo.
I would like the logo & website address www.PLUMlearnhub.example on the front of the card, all other info on the backside. The final design should communicate authority and credibility.

• verdanda

• pantones daa520 and 3f3151. Verdana for text.
• must compliment the branding occuring on the www.PLUMlearnhub.example

```html
<!DOCTYPE html>
<html lang="en">
<head>
<meta charset="utf-8">
<title>PLUMlearnhub – Business Card</title>
<link rel="stylesheet" href="https://fonts.googleapis.com/css2?family=Noto+Sans:wght@400;700;800&display=swap">
<style>
  :root {
    --gold: #daa520;
    --plum: #3f3151;
    --paper: #ffffff;
    --cream: #f3ead3;
    --pinstripe: rgba(128,128,136,.16);
    --backdrop: #e9e6e1;
  }
  * { box-sizing: border-box; margin: 0; padding: 0; }
  html, body {
    width: 1200px; height: 900px; overflow: hidden;
    background: var(--backdrop);
    font-family: "Noto Sans", Verdana, sans-serif;
    color: var(--plum);
  }
  .canvas { position: relative; width: 1200px; height: 900px; }
  .card {
    position: absolute;
    width: 560px; height: 320px;
    background: var(--paper);
    box-shadow: 0 10px 28px rgba(0,0,0,.18);
    overflow: hidden;
  }
  .card--front { left: 180px; top: 100px; }
  .card--back  { left: 460px; top: 470px; }

  /* grey pinstripe ground shared by both sides */
  .pinstripe {
    position: absolute; inset: 0;
    background: repeating-linear-gradient(90deg,
      transparent 0 11px, var(--pinstripe) 11px 12px);
  }
  .seal-pattern {
    position: absolute; left: 0; top: 0; width: 420px; height: 320px;
    background: radial-gradient(ellipse at 40% 45%, var(--cream) 0%, rgba(243,234,211,.55) 50%, rgba(255,255,255,0) 85%);
  }
  .front-brand {
    position: absolute; right: 34px; bottom: 36px;
  }
  .brand-name {
    font-weight: 800;
    color: var(--gold);
    font-size: 38px;
    letter-spacing: -0.5px;
    line-height: 1;
  }
  .front-url {
    margin-top: 10px;
    font-size: 15px;
    color: var(--plum);
    letter-spacing: .3px;
  }

  .back-band {
    position: absolute; left: 0; top: 0; bottom: 0; width: 8px;
    background: var(--plum);
  }
  .contact {
    position: absolute; left: 300px; top: 38px;
  }
  .contact__name {
    font-weight: 700; font-size: 19px; color: var(--gold);
  }
  .contact__role { font-size: 13px; margin-top: 4px; color: var(--plum); }
  .contact__list { list-style: none; margin-top: 26px; }
  .contact__list li {
    display: flex; align-items: center; gap: 10px;
    font-size: 14px; line-height: 22px; color: var(--plum);
  }
  .contact__list svg { width: 12px; height: 12px; flex: none; }

  .back-brand {
    position: absolute; left: 30px; bottom: 44px;
    display: flex; align-items: center; gap: 18px;
  }
  .brand-dot {
    width: 84px; height: 84px; border-radius: 50%;
    background: var(--gold);
  }
  .back-brand .brand-name { font-size: 40px; }
</style>
</head>
<body>
<main class="canvas">

  <section class="card card--front" aria-label="Card front">
    <div class="pinstripe" aria-hidden="true"></div>
    <div class="seal-pattern" role="img" aria-label="Faint repeating pattern of cream wax seals"></div>
    <div class="front-brand">
      <div class="brand-name">PLUMlearnhub</div>
      <div class="front-url">www.PLUMlearnhub.example</div>
    </div>
  </section>

  <section class="card card--back" aria-label="Card back">
    <div class="back-band" aria-hidden="true"></div>
    <div class="contact">
      <div class="contact__name">Dana Morrow</div>
      <div class="contact__role">Founder/CEO</div>
      <ul class="contact__list">
        <li>
          <svg viewBox="0 0 12 12" aria-hidden="true"><path fill="var(--gold)" d="M2.5 0.8l2 2-1 1.3c.6 1.5 1.9 2.8 3.4 3.4l1.3-1 2 2-1.3 1.6C5.6 10 2 6.4 .9 2.1z"/></svg>
          555.010.4821
        </li>
        <li>
          <svg viewBox="0 0 12 12" aria-hidden="true"><rect x="3" y="0.8" width="6" height="10.4" rx="1" fill="none" stroke="var(--gold)" stroke-width="1.2"/><circle cx="6" cy="9.4" r=".7" fill="var(--gold)"/></svg>
          555.010.7735
        </li>
        <li>
          <svg viewBox="0 0 12 12" aria-hidden="true"><rect x="0.5" y="2.2" width="11" height="7.6" fill="var(--gold)"/><path d="M0.8 2.6L6 6.6l5.2-4" fill="none" stroke="#fff" stroke-width="1"/></svg>
          dana@PLUMlearnhub.example
        </li>
      </ul>
    </div>
    <div class="back-brand">
      <span class="brand-dot" aria-hidden="true"></span>
      <span class="brand-name">PLUMlearnhub</span>
    </div>
  </section>

</main>
</body>
</html>
```